Freeze dried pet treats and chews packaging design

We are an Belgium based brand selling all natural treats and chews for pets. We are looking for a full color packaging design for a new line of freeze dried treats and chews for cats and dogs. The design should look familiar for our customers with our existing logo, but with a fresh new design especially for this new line. It should reflect our core values of natural, species appropriate food products without any additives or nasties.
The packaging will be a stand-up pouch with zipper, eurohole, easy open and with a window somewhere in the design to show the products inside. Please present your design as a mockup if possible.
Name of the product will be "Velmo Freeze Dried Bitzoos". Add icons to emphasize certain aspects of the product:
- 100% natural
- freeze dried (preserves all nutrients best)
- 100% mono protein
- without additives
- high in protein
- high in flavor
The design is a generic one for 12 different products, only one pouch will be produced and finished with 12 different round labels to indicate the protein source (beef, chicken, lamb, etc). You can include one of these stickers on your design to make the example complete. The sticker should have a separate color for every protein source to make it good distinguishable, an icon representing the protein source (see examples of existing packaging) and a round text around it with the protein source in text in Dutch, French and English (example: RUND - BŒUF - BEEF).
Important: after this design we need more designs for other new product lines, so the winner might get more out of this then only this one project!
High premium pet products
Petfood
- Fontastique, Roboto (used for logo and current designs), others welcome too

```html
<!DOCTYPE html>
<html lang="en">
<head>
<meta charset="utf-8">
<title>Velmo Freeze Dried Bitzoos – Pouch Front</title>
<link rel="stylesheet" href="https://fonts.googleapis.com/css2?family=Fredoka:wght@500;600;700&family=Roboto+Condensed:wght@400;700&display=swap">
<style>
  :root {
    --paper: #eeeeec;
    --paper-edge: #e2e2df;
    --green: #5cc12e;
    --green-light: #8fd45c;
    --green-dark: #3fae25;
    --purple: #6a2fa3;
    --purple-deep: #4e2391;
    --purple-soft: #8a55c2;
    --cream: #fbf6e3;
    --window: #3a2622;
    --silhouette: #8c4fd0;
    --white: #ffffff;
  }
  * { margin: 0; padding: 0; box-sizing: border-box; }
  html, body { width: 1200px; height: 1101px; overflow: hidden; background: var(--white); }
  .canvas { position: relative; width: 1200px; height: 1101px; }
  .pouch { position: absolute; left: 0; top: 0; width: 1200px; height: 1101px; }
  .title { font-family: "Fredoka", sans-serif; font-weight: 600; fill: var(--cream); }
  .brand { font-family: "Fredoka", sans-serif; font-weight: 600; fill: var(--white); }
  .arc-text { font-family: "Roboto Condensed", sans-serif; font-weight: 700; fill: var(--cream); }
  .badge-strong { font-family: "Fredoka", sans-serif; font-weight: 700; fill: var(--purple); }
  .badge-light { font-family: "Roboto Condensed", sans-serif; font-weight: 400; fill: var(--purple); }
  .claim-strong { font-family: "Fredoka", sans-serif; font-weight: 700; fill: var(--purple); }
  .claim-light { font-family: "Roboto Condensed", sans-serif; font-weight: 400; fill: var(--purple-deep); }
  .sticker-text { font-family: "Fredoka", sans-serif; font-weight: 500; fill: var(--cream); }
  .small { font-family: "Roboto Condensed", sans-serif; font-weight: 400; fill: var(--cream); }
  .small-bold { font-family: "Roboto Condensed", sans-serif; font-weight: 700; fill: var(--cream); }
</style>
</head>
<body>
<div class="canvas">
<svg class="pouch" width="1200" height="1101" viewBox="0 0 1200 1101" xmlns="http://www.w3.org/2000/svg">
  <defs>
    <linearGradient id="greenBand" x1="0" y1="0" x2="1" y2="0">
      <stop offset="0" stop-color="#8fd12e"/>
      <stop offset="1" stop-color="#45b02a"/>
    </linearGradient>
    <linearGradient id="greenFade" x1="0" y1="0" x2="0" y2="1">
      <stop offset="0" stop-color="#a9dc78"/>
      <stop offset="1" stop-color="#7fcc55"/>
    </linearGradient>
    <linearGradient id="purpleBody" x1="0" y1="0" x2="1" y2="1">
      <stop offset="0" stop-color="#8b5cc6"/>
      <stop offset="0.5" stop-color="#5f2a9e"/>
      <stop offset="1" stop-color="#4a2290"/>
    </linearGradient>
    <path id="tagline-arc" d="M497,460 Q623,366 753,458"/>
  </defs>

  <!-- pouch body -->
  <rect class="pouch-body" x="315" y="120" width="596" height="875" rx="14" fill="var(--paper)"/>
  <rect x="315" y="120" width="596" height="875" rx="14" fill="none" stroke="var(--paper-edge)" stroke-width="2"/>

  <!-- green band -->
  <rect class="green-band" x="393" y="120" width="441" height="210" fill="url(#greenBand)"/>
  <rect x="393" y="240" width="441" height="660" fill="url(#greenFade)"/>
  <rect x="393" y="900" width="441" height="95" fill="var(--green-light)"/>
  <rect x="393" y="220" width="441" height="3" fill="var(--green-dark)"/>
  <rect x="393" y="230" width="441" height="2" fill="var(--green-dark)" opacity="0.6"/>

  <!-- euro hole -->
  <rect class="euro-hole" x="564" y="166" width="94" height="24" rx="12" fill="var(--white)"/>
  <circle cx="611" cy="167" r="10" fill="var(--white)"/>

  <!-- purple panel -->
  <path class="purple-panel" d="M425,347 L808,347 L804,985 L442,985 Z" fill="url(#purpleBody)"/>
  <path d="M425,347 Q432,342 440,347 T455,347 T470,347 T485,347 T500,347 T515,347 T530,347 T545,347 T560,347 T575,347 T590,347 T605,347 T620,347 T635,347 T650,347 T665,347 T680,347 T695,347 T710,347 T725,347 T740,347 T755,347 T770,347 T785,347 T800,347 L808,347" fill="none" stroke="var(--green-light)" stroke-width="4"/>

  <!-- brand name -->
  <rect class="brand-plate" x="560" y="318" width="122" height="72" rx="8" fill="var(--purple)"/>
  <text class="brand" x="621" y="366" font-size="36" text-anchor="middle">Velmo</text>

  <!-- mono protein / natural badge -->
  <rect class="claim-badge" x="422" y="333" width="70" height="104" rx="8" fill="var(--cream)" stroke="var(--white)" stroke-width="3"/>
  <text class="badge-strong" x="457" y="362" font-size="17" text-anchor="middle">100%</text>
  <text class="badge-strong" x="457" y="374" font-size="13" text-anchor="middle">MONO</text>
  <text class="badge-light" x="457" y="387" font-size="13" text-anchor="middle">PROTEIN</text>
  <line x1="428" y1="393" x2="486" y2="393" stroke="var(--purple-soft)" stroke-dasharray="3 3"/>
  <text class="badge-strong" x="459" y="415" font-size="17" text-anchor="middle">100%</text>
  <text class="badge-light" x="459" y="429" font-size="13" text-anchor="middle">NATURAL</text>
  <circle cx="419" cy="367" r="10" fill="var(--purple)" stroke="var(--white)" stroke-width="2"/>
  <path d="M414,367 l3,4 l6,-7" fill="none" stroke="var(--white)" stroke-width="2"/>
  <circle cx="424" cy="411" r="10" fill="var(--purple)" stroke="var(--white)" stroke-width="2"/>
  <path d="M419,411 l3,4 l6,-7" fill="none" stroke="var(--white)" stroke-width="2"/>

  <!-- arched tagline -->
  <text class="arc-text" font-size="13"><textPath href="#tagline-arc" textLength="272" lengthAdjust="spacing">PRESERVES ALL NUTRIENTS BEST</textPath></text>

  <!-- dog and cat figure area -->
  <rect role="img" aria-label="Cream silhouette of a sitting dog and cat" x="590" y="442" width="50" height="44" rx="10" fill="var(--cream)" opacity="0.85"/>

  <!-- product name -->
  <text class="title" x="613" y="548" font-size="42" text-anchor="middle">DRIED BITZOOS</text>
  <text class="title" x="613" y="586" font-size="36" text-anchor="middle">VELMO FREEZE</text>
  <rect x="491" y="607" width="30" height="3" fill="var(--cream)"/>
  <rect x="706" y="606" width="30" height="3" fill="var(--cream)"/>

  <!-- product window -->
  <path role="img" aria-label="Window showing freeze dried beef chunks" d="M443,640 Q520,615 600,630 T785,638 L785,770 L446,770 Z" fill="var(--window)"/>

  <!-- pet silhouettes -->
  <path role="img" aria-label="Row of purple cat and dog silhouettes" d="M485,815 L485,772 L505,738 L540,730 L570,740 L600,735 L650,760 L690,730 L720,738 L750,745 L770,770 L775,815 Z" fill="var(--silhouette)" opacity="0.9"/>

  <!-- claims banner -->
  <rect class="claims-banner" x="474" y="805" width="326" height="62" rx="4" fill="var(--cream)"/>
  <text class="claim-strong" x="543" y="843" font-size="15" text-anchor="middle">HIGH IN</text>
  <text class="claim-light" x="543" y="861" font-size="17" text-anchor="middle">FLAVOR</text>
  <text class="claim-strong" x="645" y="842" font-size="15" text-anchor="middle">WITHOUT</text>
  <text class="claim-light" x="645" y="860" font-size="17" text-anchor="middle">ADDITIVES</text>
  <text class="claim-strong" x="740" y="842" font-size="15" text-anchor="middle">HIGH IN</text>
  <text class="claim-light" x="740" y="860" font-size="17" text-anchor="middle">PROTEIN</text>

  <!-- protein sticker -->
  <circle class="protein-sticker" cx="445" cy="840" r="46" fill="var(--cream)"/>
  <circle cx="445" cy="840" r="40" fill="var(--green)"/>
  <rect role="img" aria-label="White cow icon" x="434" y="812" width="20" height="12" rx="3" fill="var(--white)"/>
  <text class="sticker-text" x="446" y="845" font-size="13" text-anchor="middle">RUND</text>
  <text class="sticker-text" x="446" y="858" font-size="13" text-anchor="middle">BŒUF</text>
  <text class="sticker-text" x="446" y="871" font-size="13" text-anchor="middle">BEEF</text>

  <!-- net weight -->
  <text class="small" x="467" y="904" font-size="13">NET WT 20 OZ</text>
  <text class="small" x="467" y="919" font-size="13">(3.75 LB) (1.7 kg)</text>

  <!-- freeze dried note -->
  <text class="small-bold" x="763" y="892" font-size="12" text-anchor="end">FREEZE DRIED</text>
  <text class="small" x="763" y="905" font-size="12" text-anchor="end">PRESERVES ALL</text>
  <text class="small" x="763" y="918" font-size="12" text-anchor="end">NUTRIENTS BEST</text>
</svg>
</div>
</body>
</html>
```